Letterbox drop flyers for local business

I need a flyer design for my small business located in Canberra ACT called "Tallowbend Garden Care" My company is a landscaping business offering garden design, landscaping services, garden maintenance and horticultural services. I would like to have a flyer I can leave at nurseries and do letterbox drops with that highlight the professional quality of our services and also our brand feel of rural Australia and old fashioned vibe. The flyer should highlight our services and our "free quote" policy. Attached is my business logo.

Industry/Entity Type

Small Business

Font styles to use
Serif
Decorative

Colors
f37122
fcca95
ec1f27
abd036
9bcb3c

Requirements
Must have
• A list of our services and all my contact information as well as our offer for free quotes. Present this flyer and customer receives first hour of gardening free
Nice to have
• I would like the overall feel of the design to be old fashioned. Think old painted advertisments for wickam soap and brennicks biscuits, or an old dorvan pick-up truck with the dog in the back, want to highlight our quality but also give my customers a feel for our brand as a whole

```html
<!DOCTYPE html>
<html lang="en">
<head>
<meta charset="utf-8">
<title>Tallowbend Garden Care – Flyer Cards</title>
<link rel="stylesheet" href="https://fonts.googleapis.com/css2?family=Lobster&family=Righteous&family=Open+Sans:wght@400&display=swap">
<style>
  :root {
    --backdrop: #907867;
    --timber-light: #ecc792;
    --timber-mid: #e3b57c;
    --band-orange: #f37122;
    --band-orange-soft: #f08234;
    --peach: #fcca95;
    --brand-red: #ec1f27;
    --quote-green: #9bcb3c;
    --leaf-green: #2f6b34;
    --poppy: #c9655a;
    --ink: #4a3b32;
  }
  * { margin: 0; padding: 0; box-sizing: border-box; }
  html, body { width: 939px; height: 1200px; overflow: hidden; }
  body { background: var(--backdrop); position: relative; font-family: "Righteous", sans-serif; }

  .card {
    position: absolute;
    width: 688px; height: 485px;
    background: linear-gradient(100deg, var(--timber-light), var(--timber-mid) 55%, var(--timber-light));
    box-shadow: 4px 6px 10px rgba(40, 25, 15, .45);
    overflow: hidden;
  }
  .card--front { left: 96px; top: 68px; }
  .card--back  { left: 182px; top: 628px; }

  .band { position: absolute; left: 0; width: 100%; background: linear-gradient(90deg, var(--band-orange-soft), var(--band-orange) 60%, var(--band-orange-soft)); }

  .art { position: absolute; border-radius: 40px; }
  .art--flowers { background: radial-gradient(circle at 55% 35%, var(--poppy) 0 22%, transparent 45%), linear-gradient(180deg, rgba(47,107,52,.35), rgba(47,107,52,.6)); }
  .art--leaves { background: linear-gradient(160deg, rgba(47,107,52,.25), rgba(47,107,52,.55)); }

  .brand-name {
    position: absolute;
    font-family: "Lobster", cursive;
    color: var(--brand-red);
    line-height: 1;
  }
  .social-dot { position: absolute; border-radius: 50%; background: var(--peach); }

  .tagline { position: absolute; font-family: "Lobster", cursive; line-height: 1; }
  .services {
    position: absolute; list-style: none; text-align: center;
    color: var(--peach); letter-spacing: .5px;
  }
  .quote-line {
    position: absolute; left: 0; width: 100%;
    display: flex; align-items: center;
    color: var(--quote-green);
    font-family: "Righteous", sans-serif;
  }
  .quote-line .phone-icon { width: 26px; height: 22px; margin: 0 10px 0 0; }
  .quote-line .phone { font-size: 25px; letter-spacing: 1px; }

  /* front */
  .card--front .brand-name { left: 28px; top: 70px; font-size: 92px; }
  .card--front .tagline { left: 255px; top: 238px; font-size: 46px; color: var(--brand-red); }
  .card--front .services { left: 250px; top: 296px; width: 260px; font-size: 19px; line-height: 28.5px; }
  .card--front .quote-line { top: 436px; }
  .card--front .quote-line .offer { margin-left: 28px; margin-right: 34px; font-size: 19px; }

  /* back */
  .card--back .brand-name { left: 24px; top: 38px; font-size: 54px; }
  .card--back .tagline { left: 288px; top: 32px; font-size: 40px; color: var(--peach); }
  .abn { position: absolute; right: 48px; top: 86px; font-family: "Open Sans", sans-serif; font-size: 15px; color: var(--ink); }
  .specialising { position: absolute; left: 0; width: 690px; top: 152px; text-align: center; font-size: 33px; color: var(--brand-red); letter-spacing: .5px; }
  .card--back .services { left: 185px; top: 208px; width: 320px; font-size: 22px; line-height: 33.5px; }
  .contact-name { position: absolute; left: 0; width: 690px; top: 377px; text-align: center; font-family: "Open Sans", sans-serif; font-size: 21px; color: var(--ink); }
  .card--back .quote-line { top: 436px; }
  .card--back .quote-line .offer { margin-left: 28px; margin-right: 30px; font-size: 19px; }
</style>
</head>
<body>

  <section class="card card--front">
    <div class="band" style="top:20px;height:38px"></div>
    <div class="band" style="top:285px;height:155px"></div>
    <div class="band" style="top:452px;height:22px"></div>

    <div class="art art--leaves" role="img" aria-label="Line-drawn green leaves" style="left:0;top:370px;width:115px;height:115px"></div>
    <div class="art art--flowers" role="img" aria-label="Red poppies with green line-drawn leaves" style="left:540px;top:110px;width:148px;height:375px"></div>

    <div class="social-dot" style="left:593px;top:20px;width:55px;height:55px"></div>

    <div class="brand-name">Tallowbend</div>
    <div class="tagline">Garden Care</div>
    <ul class="services">
      <li>Garden Maintenance</li>
      <li>Horticultural</li>
      <li>Garden Design</li>
      <li>Landscaping</li>
    </ul>
    <div class="quote-line">
      <span class="offer">call us for your FREE QUOTE</span>
      <svg class="phone-icon" viewBox="0 0 26 22" aria-hidden="true"><path fill="currentColor" d="M2 7c0-3 5-5 11-5s11 2 11 5v2h-6V7c-2-1-8-1-10 0v2H2zM6 10h14l3 10H3z"/><circle cx="13" cy="15" r="3" fill="#f37122"/></svg>
      <span class="phone">0400555218</span>
    </div>
  </section>

  <section class="card card--back">
    <div class="band" style="top:22px;height:55px"></div>
    <div class="band" style="top:118px;height:222px"></div>
    <div class="band" style="top:420px;height:52px"></div>

    <div class="art art--flowers" role="img" aria-label="Red poppies with green line-drawn leaves" style="left:0;top:205px;width:135px;height:230px"></div>
    <div class="art art--flowers" role="img" aria-label="Red poppies with green line-drawn leaves" style="left:540px;top:110px;width:148px;height:375px"></div>

    <div class="social-dot" style="left:592px;top:24px;width:52px;height:52px"></div>

    <div class="brand-name">Tallowbend</div>
    <div class="tagline">Garden Care</div>
    <div class="abn">ABN: 12 345 678 901</div>

    <h2 class="specialising">Specialising In:</h2>
    <ul class="services">
      <li>Garden Maintenance</li>
      <li>Horticultural</li>
      <li>Garden Design</li>
      <li>Landscaping</li>
    </ul>
    <p class="contact-name">Maren Holloway</p>
    <div class="quote-line">
      <span class="offer">call us for your FREE QUOTE</span>
      <svg class="phone-icon" viewBox="0 0 26 22" aria-hidden="true"><path fill="currentColor" d="M2 7c0-3 5-5 11-5s11 2 11 5v2h-6V7c-2-1-8-1-10 0v2H2zM6 10h14l3 10H3z"/><circle cx="13" cy="15" r="3" fill="#f37122"/></svg>
      <span class="phone">0400555218</span>
    </div>
  </section>

</body>
</html>
```